BRIMLOW Pizza and Wraps

We need a website for a new restaurant called BRIMLOW "PIZZA AND WRAPS".
I have attached fonts, background images, logo, images, content etc.
can provide you with what you need to get the website design done fast and easy

I have uploaded more images of the venue and some menu items. let me know if there is anything I need to provide to make your mission clear and easy

Reason: i would like a little time to provide more feedback to designers

Industry/Entity Type

Restaurant

Coding

Coded - Design and coding required

Number of Pages Required

5+ page

Colors

Designer to choose colors to be used in the design.

Requirements
Must have
• PAGES:
• Our Story
• Menu
• Reservations
• Catering & Delivery
• Contact

```html
<!DOCTYPE html>
<html lang="en">
<head>
<meta charset="utf-8">
<title>Contact – BRIMLOW Pizza and Wraps</title>
<link rel="stylesheet" href="https://fonts.googleapis.com/css2?family=Raleway:wght@300;400;500;700;800&display=swap">
<style>
  :root {
    --ink: #333844;
    --body: #2f3138;
    --accent-frame: #d4aad0;
    --map-base: #e6e6e6;
    --brand-red: #e5202a;
    --rule: #e6e6e6;
    --social: #25272c;
    --paper: #ffffff;
  }
  * { margin: 0; padding: 0; box-sizing: border-box; }
  html, body { width: 1200px; height: 701px; overflow: hidden; background: var(--paper); }
  body { position: relative; font-family: "Raleway", sans-serif; color: var(--body); }

  .page-title {
    position: absolute; top: 42px; left: 0; width: 1200px; text-align: center;
    font-weight: 800; font-size: 44px; letter-spacing: 0; color: var(--ink);
  }

  .map-frame {
    position: absolute; left: 171px; top: 154px; width: 390px; height: 390px;
    background: var(--accent-frame); border-radius: 4px;
  }
  .map-area {
    position: absolute; left: 193px; top: 145px; width: 375px; height: 375px;
    border-radius: 6px;
    background: linear-gradient(160deg, #ececec 0%, var(--map-base) 45%, #e9e3d3 70%, #e4e4e4 100%);
  }

  .info { position: absolute; color: var(--body); }
  .info h2 { font-weight: 500; font-size: 19px; color: var(--ink); margin-bottom: 6px; }
  .info p { font-weight: 300; font-size: 15px; line-height: 27px; white-space: nowrap; }

  .hours { left: 660px; top: 162px; }
  .spacer-dot { position: absolute; font-size: 12px; font-weight: 300; }
  .delivery { left: 660px; top: 270px; }
  .address { left: 660px; top: 404px; }
  .phone { left: 891px; top: 404px; }

  .social { position: absolute; left: 891px; top: 478px; display: flex; gap: 7px; }
  .social span { width: 28px; height: 28px; border-radius: 50%; background: var(--social); display: block; }

  .footer-rule { position: absolute; left: 0; top: 616px; width: 1200px; height: 1px; background: var(--rule); }
  .brand-name {
    position: absolute; left: 150px; top: 646px;
    font-weight: 800; font-size: 23px; letter-spacing: 0.3px; color: var(--brand-red);
  }
  .copyright {
    position: absolute; right: 150px; top: 653px;
    font-weight: 400; font-size: 13px; color: var(--body);
  }
</style>
</head>
<body>
  <h1 class="page-title">CONTACT</h1>

  <div class="map-frame"></div>
  <div class="map-area" role="img" aria-label="Street map showing the restaurant location with a marker"></div>

  <section class="info hours">
    <h2>Opening Hours</h2>
    <p>Daily : 8am – 10pm</p>
    <p>Friday : Closed from Noon – 2pm</p>
  </section>
  <span class="spacer-dot" style="left:660px;top:248px;">.</span>

  <section class="info delivery">
    <h2>Delivery</h2>
    <p>Brimlow delivers directly where you want it</p>
    <p>within our coverage area.</p>
    <p>This service is available during restaurant hours.</p>
  </section>

  <section class="info address">
    <h2>Address</h2>
    <p>Larkfield, CA</p>
    <p>18 Alder Row, 2nd Fl.</p>
    <p>Larkfield, CA 95012</p>
  </section>

  <section class="info phone">
    <h2>Phone</h2>
    <p>(555) 014-2290</p>
  </section>

  <div class="social" aria-label="Social links">
    <span></span><span></span>
  </div>

  <span class="spacer-dot" style="left:856px;top:545px;">.</span>

  <div class="footer-rule"></div>
  <div class="brand-name">BRIMLOW</div>
  <div class="copyright">© Copyright 2017 Brimlow Inc.</div>
</body>
</html>
```